Brookvale Services telephone book advert

Design a tellwick directory telephone book advertisement. Attached is a current version of the brookvale services advert. Please use the same information as detailed on the existing advert but arty!. Overall size should be 130 mm by 91 mm portrait using one of the specified colours plus black. Any background should be opaque (not white). and delivered in the formats as specified.

```html
<!DOCTYPE html>
<html lang="en">
<head>
<meta charset="utf-8">
<title>Brookvale Services – Directory Advert</title>
<link href="https://fonts.googleapis.com/css2?family=Montserrat:wght@400;500&display=swap" rel="stylesheet">
<style>
  :root {
    --navy: #1d5078;
    --navy-deep: #173f60;
    --ice: #d9eaf8;
    --blush: #f6b8b2;
    --coral: #e9736c;
    --paper: #ffffff;
  }
  html, body {
    margin: 0;
    width: 960px;
    height: 1200px;
    overflow: hidden;
    background: var(--paper);
    font-family: "Montserrat", sans-serif;
  }
  .advert {
    position: absolute;
    left: 70px;
    top: 14px;
    width: 820px;
    height: 1170px;
    background: var(--navy);
    color: var(--ice);
    overflow: hidden;
  }
  .phone-art {
    position: absolute;
    left: 42px;
    top: 30px;
    width: 152px;
    height: 168px;
    border-radius: 30px;
    background: radial-gradient(circle at 50% 50%, var(--coral) 0 45%, rgba(233,115,108,0) 70%);
  }
  .phone-number {
    position: absolute;
    left: 216px;
    top: 188px;
    transform: translate(-50%, -50%) rotate(-25deg);
    font-size: 98px;
    font-weight: 500;
    letter-spacing: 2px;
    white-space: nowrap;
    color: var(--ice);
  }
  .hero-art {
    position: absolute;
    left: 310px;
    top: 18px;
    width: 500px;
    height: 392px;
    background: radial-gradient(ellipse 224px 128px at 224px 262px, var(--navy-deep) 0 98%, rgba(23,63,96,0) 100%),
                radial-gradient(ellipse 160px 150px at 250px 150px, rgba(74,150,214,0.55) 0 60%, rgba(74,150,214,0) 100%);
  }
  .company-name {
    position: absolute;
    left: 0;
    width: 100%;
    top: 418px;
    margin: 0;
    text-align: center;
    font-size: 70px;
    font-weight: 500;
    letter-spacing: 1px;
    white-space: nowrap;
  }
  .services {
    position: absolute;
    left: 0;
    width: 100%;
    top: 540px;
    margin: 0;
    text-align: center;
    font-size: 30px;
    line-height: 41px;
    font-weight: 500;
  }
  .contact {
    position: absolute;
    left: 0;
    width: 100%;
    top: 816px;
    text-align: center;
  }
  .contact p { margin: 0; white-space: nowrap; }
  .role { color: var(--blush); font-size: 30px; line-height: 40px; font-weight: 500; }
  .person { font-size: 50px; line-height: 62px; font-weight: 500; }
  .email, .more-info { color: var(--blush); font-size: 30px; line-height: 38px; font-weight: 500; }
  .website { font-size: 44px; line-height: 56px; font-weight: 500; }
  .address { font-size: 32px; line-height: 41px; font-weight: 500; }
</style>
</head>
<body>
  <main class="advert">
    <div class="phone-art" role="img" aria-label="Illustration of a ringing red retro telephone"></div>
    <div class="phone-number">318-640</div>
    <div class="hero-art" role="img" aria-label="Illustration of a smiling drain engineer in blue overalls climbing out of a manhole, giving a thumbs up, with a toolbox, hammer, spanners and pliers around"></div>

    <h1 class="company-name">Brookvale Services</h1>

    <p class="services">
      Home Buyer Surveys<br>
      Emergencies: Unblocking &amp; high pressure<br>
      cleaning Maintenance: Jetting, de-scaling &amp; root<br>
      cutting Survey: Modern CCTV, condition reports<br>
      Rehabilitation: Structural re-lining of damaged<br>
      and leaky drains
    </p>

    <section class="contact">
      <p class="role">Contracts Manager</p>
      <p class="person">Callum Hartwell</p>
      <p class="email">email: office@brookvale.gg</p>
      <p class="more-info">For more information please visit our website:</p>
      <p class="website">www.brookvale.gg</p>
      <p class="address">Kestrel Lane, Harbourside,<br>Islemere IS2 4JW</p>
    </section>
  </main>
</body>
</html>
```